graphic design for music festival

Need a design for webpage header and facebook a music festival that fits the location.

A logo type header that can overly on header with Marrowvale Music Festival in it !

the location is airlie beach whitsundays and it is called the

Marrowvale Music Festival
8th/9th/10th November 2013
65 bands over 3 days 16 venues

the bands are like lindy forsgrave, tin pelicans, dale hoskin etc..

they have started a facebook page called marrowvale music festival

need a theme/style to use for facebook cover and a header for webpages.

Reason: still need work and changing to commiting to pay !

ive gone to commit to pay for a design and added 7 days

Target Market(s)

music people who like the artists in question middle aged australians who like music really

Industry/Entity Type

Graphic Design

Requirements
Must have
• header desgin for webpages and facebook

```html
<!DOCTYPE html>
<html lang="en">
<head>
<meta charset="utf-8">
<title>Marrowvale Music Festival — Header</title>
<link rel="stylesheet" href="https://fonts.googleapis.com/css2?family=Cinzel:wght@700;900&display=swap">
<style>
  :root {
    --band-blue: #1f9ff0;
    --band-light: #8fd6ff;
    --band-bottom: #1a8de6;
    --band-bottom-dark: #1478d0;
    --title-blue: #1b8de2;
    --crowd-navy: #0d2a5c;
    --crowd-mid: #27508f;
    --haze-white: #f3f6fb;
    --haze-grey: #cfd9ea;
    --stage-blue: #3f6cb8;
    --ring-blue: #1c8fe8;
    --figure-blue: #2a86d6;
  }
  html, body {
    margin: 0;
    padding: 0;
    overflow: hidden;
    background: #ffffff;
  }
  .header {
    position: relative;
    width: 1200px;
    height: 372px;
    overflow: hidden;
    font-family: "Cinzel", "Times New Roman", serif;
  }

  /* Stage photograph area */
  .stage-scene {
    position: absolute;
    left: 0; top: 44px;
    width: 1200px; height: 278px;
    background:
      /* crowd along the bottom, dark on the left, hazy on the right */
      linear-gradient(to bottom, rgba(13,42,92,0) 0%, rgba(13,42,92,0) 50%, rgba(13,42,92,0.55) 78%, rgba(13,42,92,0.8) 100%),
      /* light haze behind the lettering */
      radial-gradient(ellipse 420px 170px at 720px 90px, rgba(255,255,255,0.95) 0%, rgba(255,255,255,0) 100%),
      /* overall tone: crowd-dark left, bright centre, blue stage right */
      linear-gradient(to right, var(--crowd-navy) 0%, var(--crowd-mid) 16%, #8ea7cf 28%, var(--haze-grey) 36%, var(--haze-white) 52%, #eef3fa 70%, #c3d3ec 86%, var(--stage-blue) 100%);
  }

  .band-top {
    position: absolute;
    left: 0; top: 0;
    width: 1200px; height: 52px;
    background: linear-gradient(to bottom, var(--band-blue) 0%, var(--band-blue) 60%, var(--band-light) 84%, rgba(255,255,255,0) 100%);
  }
  .band-bottom {
    position: absolute;
    left: 0; top: 316px;
    width: 1200px; height: 56px;
    background: linear-gradient(to bottom, rgba(255,255,255,0) 0%, var(--band-light) 10%, var(--band-bottom) 26%, var(--band-bottom-dark) 100%);
  }

  .inset-photo {
    position: absolute;
    left: 84px; top: 172px;
    width: 160px; height: 160px;
    border-radius: 50%;
    border: 6px solid var(--ring-blue);
    box-shadow: 0 0 0 2px #ffffff, 0 2px 6px rgba(0,0,0,0.35);
    background: linear-gradient(to bottom, #7d8794 0%, #c9d0d8 30%, #6c7480 55%, #1f2227 78%, #0b0c0f 100%);
  }

  .jump-figure {
    position: absolute;
    left: 416px; top: 86px;
    width: 88px; height: 134px;
    border-radius: 18px;
    background: linear-gradient(to bottom, rgba(42,134,214,0.75) 0%, rgba(42,134,214,0.55) 100%);
  }

  .festival-text {
    position: absolute;
    left: 470px; top: 0;
    width: 680px; height: 372px;
    margin: 0;
    text-align: center;
    color: var(--title-blue);
    font-weight: 700;
    text-shadow: 0 0 2px #fff, 0 0 3px #fff, 0 0 5px #fff, 1px 2px 3px rgba(0,40,90,0.35);
  }
  .festival-text span {
    position: absolute;
    left: 0; width: 100%;
    display: block;
    white-space: nowrap;
  }
  .title-name { top: 78px; font-size: 60px; line-height: 64px; font-weight: 900; }
  .title-sub { top: 148px; font-size: 38px; line-height: 42px; }
  .details-dates { top: 190px; font-size: 34px; line-height: 42px; }
  .details-dates sup { font-size: 19px; vertical-align: 14px; line-height: 0; }
  .details-lineup { top: 234px; font-size: 36px; line-height: 44px; }
</style>
</head>
<body>
  <div class="header">
    <div class="stage-scene" role="img" aria-label="Concert crowd with raised hands in front of bright blue stage lights"></div>
    <div class="band-top"></div>
    <div class="band-bottom"></div>
    <div class="inset-photo" role="img" aria-label="Circular photo of a band performing on a smoky, backlit stage"></div>
    <div class="jump-figure" role="img" aria-label="Blue silhouette of a person jumping with arms raised"></div>
    <h1 class="festival-text">
      <span class="title-name">MARROWVALE</span>
      <span class="title-sub">MUSIC FESTIVAL</span>
      <span class="details-dates">8<sup>TH</sup>/9<sup>TH</sup>/10<sup>TH</sup> NOVEMBER 2013</span>
      <span class="details-lineup">65 BANDS OVER 3 DAYS 16 VENUES</span>
    </h1>
  </div>
</body>
</html>
```